Hotel Newsletter Design

We need 4 newsletter templates for a luxurious hotel. The templates only differ in the headers (basically each has different images based on a certain theme and/or distinguishing colours). Please feel free to use other colour that those on the webpage of the hotel.

Previous newsletters were these:

"Wine bar" - http://www.marbleoakinn.example/newsletter.php?id=76&lang=en
"Feast" - http://www.marbleoakinn.example/newsletter.php?id=75&lang=en
"Hotel" - http://www.marbleoakinn.example/newsletter.php?id=77&lang=en
"Restaurant" - http://www.marbleoakinn.example/newsletter.php?id=78&lang=en

These were too basic and old-fashioned, we need something more UP-TO-DATE, FRESH, MORE MODERN DESIGN.

The final newsletter will be an HTML page with an editable section.

So upon designing please pay attention to leave a space for editable content, which is going to be text and images.

Header and footer required, these won't be editable.

The 4 different header themes are Wine bar, Hotel, Feast, Restaurant.

the website of the hotel:
http://www.marbleoakinn.example/
images that can be used:
http://www.vextrapod.example/temp/bemo/images.zip

Target Market(s)

Luxurious Hotel Visitors

Industry/Entity Type

Hospitality

Requirements
Must have
• Logo in the header, address and contact in the footer
Nice to have
• Modern design
Should not have
• Old fashioned design

```html
<!DOCTYPE html>
<html lang="en">
<head>
<meta charset="utf-8">
<title>Marble Oak Inn – Feast Newsletter</title>
<link rel="stylesheet" href="https://fonts.googleapis.com/css2?family=Arimo:wght@400;700&display=swap">
<style>
  :root {
    --page-wood: #24150f;
    --page-wood-light: #2f1c14;
    --card-body: #21130d;
    --header-panel: #3d1f15;
    --header-panel-dark: #2a150e;
    --accent-red: #b3302a;
    --heading: #d9d5d2;
    --body-text: #cfc9c5;
    --link: #e2ddd9;
    --visited: #b9b2ad;
    --button-top: #8a8a8a;
    --button-bottom: #555;
    --button-text: #f2f2f2;
  }
  * { box-sizing: border-box; margin: 0; padding: 0; }
  html, body { width: 1200px; height: 900px; overflow: hidden; }
  body {
    font-family: "Arimo", Arial, sans-serif;
    background: linear-gradient(90deg, var(--page-wood) 0%, var(--page-wood-light) 30%, var(--page-wood) 55%, var(--page-wood-light) 80%, var(--page-wood) 100%);
    position: relative;
  }
  .newsletter {
    position: absolute;
    left: 20px; top: 44px;
    width: 1140px; height: 900px;
    border-radius: 22px 22px 0 0;
    overflow: hidden;
    background: var(--card-body);
  }
  .masthead { display: flex; height: 332px; }
  .masthead-photo {
    width: 624px; height: 100%;
    background:
      radial-gradient(ellipse at 30% 80%, rgba(120,20,30,.9) 0%, rgba(120,20,30,0) 35%),
      radial-gradient(ellipse at 55% 30%, rgba(170,60,30,.8) 0%, rgba(170,60,30,0) 40%),
      radial-gradient(ellipse at 80% 70%, rgba(190,160,110,.6) 0%, rgba(190,160,110,0) 35%),
      linear-gradient(135deg, #8a5a32 0%, #5e3019 40%, #3a1a10 100%);
  }
  .masthead-brand {
    flex: 1;
    background: linear-gradient(90deg, var(--header-panel-dark), var(--header-panel) 50%, var(--header-panel-dark));
    display: flex; flex-direction: column; align-items: center;
    padding-top: 70px;
  }
  .masthead-tagline { color: var(--accent-red); font-size: 36px; font-weight: 400; }
  .brand-name {
    margin-top: 100px;
    color: var(--accent-red);
    font-size: 22px; letter-spacing: 3px; text-transform: uppercase;
  }
  .editable { position: relative; padding: 0 48px 0 36px; }
  .section-title { color: var(--heading); font-size: 34px; font-weight: 700; }
  .welcome-title { position: absolute; left: 36px; top: 34px; }
  .welcome-text {
    position: absolute; left: 36px; top: 108px; width: 434px;
    color: var(--body-text); font-size: 16.5px; line-height: 23px; text-align: justify;
  }
  .welcome-text a { color: var(--link); }
  .welcome-text a.visited { color: var(--visited); }
  .read-more {
    position: absolute; left: 40px; top: 268px;
    width: 132px; height: 36px; border-radius: 8px;
    background: linear-gradient(var(--button-top), var(--button-bottom));
    color: var(--button-text); font-size: 16px; line-height: 36px; text-align: center;
    text-decoration: none; box-shadow: 0 1px 2px rgba(0,0,0,.6);
  }
  .feature-photo {
    position: absolute; left: 484px; top: 104px;
    width: 608px; height: 272px;
    border: 2px solid #111;
    background: linear-gradient(180deg, #c9a46a 0%, #7a4a24 30%, #4a2614 60%, #e8e4dc 62%, #cfcac2 100%);
  }
  .second-title { position: absolute; left: 36px; top: 444px; }
  .second-text {
    position: absolute; left: 36px; top: 512px; width: 1080px;
    color: var(--body-text); font-size: 16.5px; line-height: 23px; white-space: nowrap;
  }
  .second-text sup { font-size: 12px; }
</style>
</head>
<body>
  <main class="newsletter">
    <header class="masthead">
      <div class="masthead-photo" role="img" aria-label="Feast table with red wine, bowls of pasta and a basket of vegetables"></div>
      <div class="masthead-brand">
        <p class="masthead-tagline">Make it a Feast!</p>
        <p class="brand-name">Marble Oak Inn</p>
      </div>
    </header>
    <section class="editable">
      <h2 class="section-title welcome-title">Welcome</h2>
      <p class="welcome-text">Lorem ipsum dolor sit amet, <a href="#">link</a>, <a class="visited" href="#">visited link</a>, hovered link consectetuer adipiscing elit. Quisque sed felis. Aliquam sit amet felis. Mauris semper, velit semper laoreet dictum, quam diam dictum urna, nec placerat elit nisl in quam. Etiam augue pede, molestie eget, rhoncus at, convallis ut, eros.</p>
      <a class="read-more" href="#">Read more...</a>
      <div class="feature-photo" role="img" aria-label="Close-up of a grand piano keyboard under warm light"></div>
      <h2 class="section-title second-title">Text, Link, Visited, Hovered</h2>
      <p class="second-text">Lorem <sup>superscript</sup> dolor sit amet, consectetuer adipiscing elit. text link Nullam dignissim convallis est. Quisque aliquam. Aene</p>
    </section>
  </main>
</body>
</html>
```